Corrigan Architecture (business card)

We need a business card design. We are a full service architectural firm that specializes in mostly residential projects and some commercial projects. We are located in Hudson Valley, New York. We work with high end clients and want a business card that is memorable and has a sleek, modern, design but will not go out of style (timeless).

Target Market(s)

high end residential clients

Industry/Entity Type

Architect

Contact Information for Business Card

Front of card
Company Logo
website: www.corriganarchitectur.example
what we do: residential, Commercial

back of card
Owner's Name: Dorian Corrigan
owner's title: Principal
Business address: 2873 Route 92 Suite A, Brellfordton, NY 12688
phone number: 845-608-2917
e-mail: dc@corriganarchitecture.example

We like:
icons
sleek and clean design
simple not too busy or too much text

Font styles to use
Sans Serif

Colors
0356a4

Requirements
Must have
• company colors are navy blue, white, and gray
• Front of card
• Company Logo
• website: www.corriganarchitectur.example
• what we do: residential, Commercial
• back of card
• Owner's Name: Dorian Corrigan
• owner's title: Principal
• Business address: 2873 Route 92 Suite A, Brellfordton, NY 12688
• phone number: 845-608-2917
• e-mail: dc@corriganarchitecture.example
Nice to have
• We like:
• icons
• sleek and clean design
• simple not too much text
• color of the card to be either blue or gray
Should not have
• we do not like houses in the design or plans of houses-this is over done and we don't like it.
• no QR CODES

```html
<!DOCTYPE html>
<html lang="en">
<head>
<meta charset="utf-8">
<title>Corrigan Architecture – Business Card</title>
<link rel="stylesheet" href="https://fonts.googleapis.com/css2?family=Jost:wght@400&family=Arimo:wght@400;700&display=swap">
<style>
  :root {
    --navy: #23205f;
    --gray: #7b7b7b;
    --white: #ffffff;
    --stage: #e4e4e4;
    --edge: #d2d2d2;
  }
  * { margin: 0; padding: 0; box-sizing: border-box; }
  html, body { width: 1200px; height: 802px; overflow: hidden; background: var(--stage); }
  .canvas { position: relative; width: 1200px; height: 802px; }

  .card {
    position: absolute; top: 274px; width: 443px; height: 264px;
    background: var(--white); overflow: hidden;
    box-shadow: 0 0 0 1px var(--edge);
  }
  .card--back { left: 152px; }
  .card--front { left: 624px; }

  /* back of card */
  .gray-band { position: absolute; left: 21px; top: 0; width: 143px; height: 100%; background: var(--gray); }
  .navy-panel { position: absolute; left: 186px; top: 0; width: 257px; height: 100%; background: var(--navy); color: var(--white); }

  .wordmark {
    font-family: "Jost", sans-serif; font-weight: 400;
    font-variant: small-caps; letter-spacing: 0.5px; line-height: 1;
  }
  .back-wordmark { position: absolute; left: 22px; top: 28px; font-size: 28px; line-height: 29px; color: var(--white); }

  .person { position: absolute; left: 22px; top: 107px; font-family: "Arimo", sans-serif; }
  .person__name { font-weight: 700; font-size: 14.5px; letter-spacing: 0.3px; text-transform: uppercase; }
  .person__title { font-size: 12.5px; margin-top: 1px; }

  .contact { position: absolute; left: 22px; top: 147px; list-style: none; font-family: "Arimo", sans-serif; font-size: 12px; }
  .contact li { display: flex; align-items: center; gap: 4px; height: 16.5px; }
  .contact svg { width: 12px; height: 12px; flex: none; }

  .address { position: absolute; left: 24px; top: 202px; font-family: "Arimo", sans-serif; font-size: 12.5px; line-height: 16px; font-style: normal; }

  /* front of card */
  .front-logo { position: absolute; left: 70px; top: 91px; display: flex; align-items: center; gap: 13px; }
  .front-logo__square { width: 52px; height: 57px; background: var(--navy); flex: none; }
  .front-wordmark { font-size: 31px; line-height: 33px; color: var(--navy); }

  .services {
    position: absolute; left: 0; width: 100%; top: 214px; text-align: center;
    font-family: "Jost", sans-serif; font-size: 12.5px; letter-spacing: 0.4px; color: var(--navy);
  }
  .services__divider { margin: 0 4px; }
</style>
</head>
<body>
<main class="canvas">

  <section class="card card--back" aria-label="Back of card">
    <div class="gray-band"></div>
    <div class="navy-panel">
      <div class="wordmark back-wordmark">Corrigan<br>Architecture</div>

      <div class="person">
        <div class="person__name">Dorian Corrigan</div>
        <div class="person__title">Principal</div>
      </div>

      <ul class="contact">
        <li>
          <svg viewBox="0 0 12 12" aria-hidden="true"><rect x="0.6" y="0.6" width="10.8" height="10.8" rx="1.5" fill="none" stroke="#fff" stroke-width="1.1"/><path d="M3.4 2.8c.4-.3.8-.2 1 .2l.6 1.1c.2.3.1.6-.2.8l-.4.3c.4.9 1 1.5 1.9 1.9l.3-.4c.2-.3.5-.4.8-.2l1.1.6c.4.2.5.6.2 1l-.4.5c-.3.4-.8.5-1.3.3-2-.8-3.4-2.2-4.2-4.2-.2-.5-.1-1 .3-1.3z" fill="#fff"/></svg>
          845-608-2917
        </li>
        <li>
          <svg viewBox="0 0 12 12" aria-hidden="true"><rect x="0.5" y="2.3" width="11" height="7.6" fill="#fff"/><path d="M0.8 2.8 6 7 11.2 2.8" fill="none" stroke="#23205f" stroke-width="1"/></svg>
          dc@corriganarchitecture.example
        </li>
        <li>
          <svg viewBox="0 0 12 12" aria-hidden="true"><g fill="none" stroke="#fff" stroke-width="1"><circle cx="6" cy="6" r="5.3"/><ellipse cx="6" cy="6" rx="2.4" ry="5.3"/><path d="M0.8 6h10.4M1.6 3.3h8.8M1.6 8.7h8.8"/></g></svg>
          www.corriganarchitectur.example
        </li>
      </ul>

      <address class="address">2873 Route 92 Suite A<br>Brellfordton, NY 12688</address>
    </div>
  </section>

  <section class="card card--front" aria-label="Front of card">
    <div class="front-logo">
      <span class="front-logo__square" aria-hidden="true"></span>
      <div class="wordmark front-wordmark">Corrigan<br>Architecture</div>
    </div>
    <p class="services">RESIDENTIAL<span class="services__divider">|</span>COMMERCIAL</p>
  </section>

</main>
</body>
</html>
```